Australian Meat, Seafood and Fresh Produce Website

Our organization is looking to design a simple, but eye catching website to show our services.
Our company exports West Australian FRESH fruit and vegetables, seafood and meat.
The website we are looking for would consist of:
- Landing Page
- Company info
- Directors bio
- Page that highlights our products
- Contact us page
We would like it to have a Chinese translated version as well.
Milo
Target Market(s)
Chinese Market
Industry/Entity Type
It Company
Number of Pages Required
1 page
Look and feel
Each slider illustrates characteristics of the customer's brand and the style your logo design should communicate.

```html
<!DOCTYPE html>
<html lang="en">
<head>
<meta charset="utf-8">
<title>Coastline Harvest</title>
<link href="https://fonts.googleapis.com/css2?family=Raleway:wght@400;500;600;700&family=Open+Sans:wght@400;600;700&display=swap" rel="stylesheet">
<style>
:root{
  --ink:#333333;
  --muted:#666666;
  --accent-red:#cc2a0c;
  --hero-red:rgba(214,52,14,.9);
  --band-blue:#1a82cf;
  --band-blue-deep:#0d5fa8;
  --footer:#0b0b0b;
  --page:#ffffff;
  --hero-grey:#e4e4e4;
  --flag:#4a5d9a;
}
*{margin:0;padding:0;box-sizing:border-box}
html,body{width:937px;height:1200px;overflow:hidden;background:var(--page)}
body{position:relative;font-family:"Open Sans",sans-serif;color:var(--ink)}
.abs{position:absolute}

.site-header{position:absolute;left:0;top:0;width:937px;height:76px}
.brand{left:162px;top:27px;font-family:"Open Sans",sans-serif;font-size:17px;font-weight:600;color:var(--ink);white-space:nowrap}
.main-nav{left:389px;top:33px;font-family:"Raleway",sans-serif;font-size:11px;color:var(--ink)}
.main-nav span{position:absolute;white-space:nowrap}
.lang-select{left:705px;top:30px;width:67px;height:19px;border:1px solid #d6d6d6;display:flex;align-items:center;padding-left:7px;gap:5px;font-size:8px;color:var(--ink)}
.lang-select .flag{width:12px;height:8px;background:var(--flag)}
.lang-select .caret{width:0;height:0;border-left:3px solid transparent;border-right:3px solid transparent;border-top:4px solid #777;margin-left:3px}

.hero{left:0;top:76px;width:937px;height:320px;background:linear-gradient(#f0f0f0,var(--hero-grey) 60%,#ececec)}
.hero-photo{left:165px;top:0;width:606px;height:320px;background:linear-gradient(135deg,#8c3b2c 0%,#b65a4a 30%,#6c5148 55%,#3d3a3c 80%,#7a4a40 100%)}
.hero-card{left:184px;top:108px;width:272px;height:104px;background:var(--hero-red);color:#fff;padding:13px 0 0 32px}
.hero-card h1{font-weight:400;font-size:24px;line-height:26px;white-space:nowrap}
.hero-card h2{font-weight:400;font-size:16px;line-height:20px}
.hero-card p{font-size:7.6px;line-height:13px;margin-top:4px;width:220px}
.hero-dots{left:453px;top:292px;display:flex;gap:3px}
.hero-dots i{width:13px;height:13px;border-radius:50%;background:#fff;display:block}

.about{left:0;top:430px;width:937px;text-align:center}
.about h2{font-family:"Raleway",sans-serif;font-weight:400;font-size:21px;color:#222}
.about p{font-size:8.3px;line-height:13px;color:var(--muted);width:580px;margin:10px auto 0}
.about p.small{font-size:6.9px;width:600px;margin-top:5px}

.products{left:0;top:578px;width:937px;height:257px;background:linear-gradient(100deg,var(--band-blue) 0%,#2a8fd6 45%,var(--band-blue-deep) 100%);text-align:center;color:#fff}
.notch{left:452px;top:578px;width:0;height:0;border-left:17px solid transparent;border-right:17px solid transparent;border-top:16px solid #fff}
.products h2{font-family:"Raleway",sans-serif;font-weight:500;font-size:17px;margin-top:37px}
.products p{font-size:7.4px;line-height:13px;width:480px;margin:6px auto 0;color:#e8f2fb}
.product-card{top:104px;width:143px;height:109px;background:#f4f4f4;box-shadow:0 2px 4px rgba(0,0,0,.25)}
.product-card .thumb{width:143px;height:84px}
.product-card .label{height:25px;line-height:25px;font-family:"Raleway",sans-serif;font-weight:700;font-size:12px;color:var(--accent-red);text-align:center;background:rgba(255,255,255,.92)}

.team{left:165px;top:876px;width:610px}
.team h2{font-family:"Raleway",sans-serif;font-weight:400;font-size:20px;color:var(--ink)}
.member{width:295px}
.member h3{font-family:"Raleway",sans-serif;font-weight:400;font-size:12px;color:var(--accent-red)}
.member p{font-size:7.1px;line-height:13px;color:var(--muted);margin-top:3px}
.member a{display:block;font-size:8.6px;color:var(--ink);text-decoration:none;margin-top:9px}

.site-footer{left:0;top:1123px;width:937px;height:77px;background:var(--footer);color:#fff}
.footer-nav span{position:absolute;top:19px;font-family:"Raleway",sans-serif;font-size:10.5px;white-space:nowrap}
.legal{left:165px;top:41px;font-size:7px;color:#bbb}
.social{left:687px;top:24px;display:flex;gap:7px}
.social i{display:block;width:11px;height:11px;border-radius:50%;background:#fff}
</style>
</head>
<body>

<header class="site-header">
  <div class="abs brand">Coastline Harvest</div>
  <nav class="abs main-nav">
    <span style="left:0">Home</span>
    <span style="left:53px">About Us</span>
    <span style="left:123px">Bio</span>
    <span style="left:163px">Products</span>
    <span style="left:231px">Contact us</span>
  </nav>
  <div class="abs lang-select"><span class="flag"></span>English<span class="caret"></span></div>
</header>

<section class="abs hero">
  <div class="abs hero-photo" role="img" aria-label="Busy market stall with fresh cuts of meat hanging above the counter"></div>
  <div class="abs hero-card">
    <h1>Supply high quality</h1>
    <h2>West Australian produce</h2>
    <p>Sed porta Suspendisse quam leo molestie sed luctus quis feugiat in pede Fusce tellus Sed metus augue</p>
  </div>
  <div class="abs hero-dots"><i></i><i></i><i></i></div>
</section>

<section class="abs about">
  <h2>ABOUT OUR COMPANY</h2>
  <p>Coastline Harvest (CH) aims to supply high quality West Australian produce to the rest of the World. Western Australia is known for its high quality farming practices and environment, which produces meat, seafood, fruit and vegetable of a caliber that is respected globally.</p>
  <p class="small">With a management team and first class suppliers allows our organization to provide quality ingredients, straight from farm or ocean to purchaser, in a timely manner to the highest quality.This document aims to outline both our management team and their back grounds, as well as the suppliers who will initially be supply our global customers.</p>
</section>

<section class="abs products">
  <h2>PRODUCT WE SUPPLIES</h2>
  <p>Vivamus porttitor purus nisi eleifend libero a tempus libero lectus feugiat felis Morbi diam mauris viverra in gravida eu mattis in ante Morbi eget arcu Morbi porta libero id ullamcorper nonummy nibh ligula pulvinar metus eget consectetuer augue nisi quis lacus</p>
  <div class="abs product-card" style="left:165px">
    <div class="thumb" role="img" aria-label="Basket of fresh vegetables" style="background:linear-gradient(135deg,#5f8a2c,#a8602c 60%,#7a4a24)"></div>
    <div class="label">Vegetables</div>
  </div>
  <div class="abs product-card" style="left:319px">
    <div class="thumb" role="img" aria-label="Assorted colourful fruit" style="background:linear-gradient(135deg,#c9531a,#a81f1a 50%,#5d7a26)"></div>
    <div class="label">Fruits</div>
  </div>
  <div class="abs product-card" style="left:475px">
    <div class="thumb" role="img" aria-label="Fresh whole fish on ice" style="background:linear-gradient(135deg,#6f6d6a,#b7b3ad 50%,#4a4644)"></div>
    <div class="label">Sea Food</div>
  </div>
  <div class="abs product-card" style="left:630px">
    <div class="thumb" role="img" aria-label="Packaged cuts of red meat" style="background:linear-gradient(135deg,#d9a6a2,#b0222a 55%,#e6c9c6)"></div>
    <div class="label">Meat</div>
  </div>
</section>
<div class="abs notch"></div>

<section class="abs team">
  <h2>The Management Team</h2>
  <div class="abs member" style="left:0;top:42px">
    <h3>Aaron Whitlock</h3>
    <p>Aaron brings with him decades of experience in hospitality management, specializing in remote service and major city hospitality catering management. Whilst managing remote sites through Australia and off shore rigs, Aaron's management skills</p>
    <a>Learn More</a>
  </div>
  <div class="abs member" style="left:313px;top:38px">
    <h3>Daniel Ho</h3>
    <p>Daniel has been in the Sales, Retail &amp; Procurement since 1972, after leaving Senior High School started Sales in the Tobacco industry before taking up Retail position in Supermarket management.</p>
    <a>Learn More</a>
  </div>
  <div class="abs member" style="left:0;top:144px">
    <h3>Simon Barrett</h3>
    <p>Senior Executive with entrepreneurial experience in company building mainly in the transport and logistics field. In excess of 30 years operational and strategic experience in running transport companies with national and international reach</p>
    <a>Learn More</a>
  </div>
  <div class="abs member" style="left:314px;top:144px">
    <h3>Dr Meihua Tan</h3>
    <p>Well respected senior professional in the health and business community of Shunde Peoples Republic of China. Meihua has worked in the health sector in Shunde for many years and has progressed to a senior management position</p>
    <a>Learn More</a>
  </div>
</section>

<footer class="abs site-footer">
  <nav class="footer-nav">
    <span style="left:165px">Home</span>
    <span style="left:218px">About Us</span>
    <span style="left:288px">Bio</span>
    <span style="left:328px">Products</span>
    <span style="left:396px">Contact us</span>
  </nav>
  <div class="abs legal">© 2015 Company Name &nbsp;All right reserved &nbsp;Term of Use</div>
  <div class="abs social" aria-label="Social links"><i></i><i></i><i></i><i></i></div>
</footer>

</body>
</html>
```